Military training songs recorded live with troops.

I need a graphic designer (and website builder) to create the artwork, logo and website for a new company marketing campaign under the URL www.marchfolio.com.
This website will be devoted to featuring the audio catalog I created with my father in which we recorded live during PT training with troops of the Varden Guard.
Ultimately, I would like the website to be the one and only distribution site for our catalog. This will be the most effectively means in addressing piracy and copyright infringement. However, this would require a website platform which supports MP3 and financial sales software.
Thus, for now, the website can establish and feature the catalog we created and provide links just to Zelpora.
Thus in addition to a website, we would need graphics for the new covers for our catalog which contains 32 products.
I have attached a MP3 file to provide insight into the military cadences we recorded and have the exclusive rights to distribute and sell.

Target Market(s)

For the representation of military service to our entire society.

Industry/Entity Type

One-of-a-kind military training songs recorded live with troops during PT runs & marches.

Coding

Coded - Design and coding required

Number of Pages Required

5+ page

Other font styles liked:
• Lordcorps

Colors

Designer to choose only greyscale colors for use in the design.

Requirements
Must have
• To feature the entire catalog by creating artwork for every product (cover art needed for 32 products) and separating the products under the various Armed Force: The Varden Tidal Corps, the Army, the Air Force and the Navy. Every product must have a link for purchase from Zelpora.
Nice to have
• The ability to play MP3 files.
Should not have
• N/A

```html
<!DOCTYPE html>
<html lang="en">
<head>
<meta charset="utf-8">
<title>Marchfolio — Military Training Music</title>
<link href="https://fonts.googleapis.com/css2?family=Anton&family=Oswald:wght@400;500;600&family=Roboto:wght@300;400&display=swap" rel="stylesheet">
<style>
:root{
  --bg:#1a1a1a;
  --panel:#222222;
  --panel-2:#252525;
  --line:#3a3a3a;
  --accent:#555555;
  --accent-text:#7d7d7d;
  --light:#c6c6c6;
  --light-dark:#a4a4a4;
  --white:#f0f0f0;
  --muted:#a8a8a8;
  --dim:#7a7a7a;
}
*{box-sizing:border-box;margin:0;padding:0}
html,body{width:675px;height:1200px;overflow:hidden;background:var(--bg)}
body{position:relative;font-family:'Roboto',sans-serif;color:var(--white)}
.abs{position:absolute}
.cond{font-family:'Oswald',sans-serif;text-transform:uppercase}
.display{font-family:'Anton',sans-serif}

/* hero */
.hero-art{left:0;top:0;width:675px;height:457px;
  background:radial-gradient(ellipse 130px 90px at 400px 125px,#8a8a8a 0%,#555 35%,transparent 75%),
  radial-gradient(ellipse 360px 220px at 420px 230px,#3c3c3c 0%,#262626 55%,transparent 100%),
  linear-gradient(180deg,#1e1e1e 0%,#262626 45%,#1b1b1b 100%)}
.hero-fade{left:0;top:0;width:300px;height:457px;background:linear-gradient(90deg,rgba(24,24,24,.9),rgba(24,24,24,0))}
.topbar{top:9px;right:0;height:12px;display:flex;font-size:6.5px;letter-spacing:.3px;color:var(--muted)}
.topbar span{padding:0 15px;border-right:1px solid var(--line)}
.menu-icon{right:14px;top:11px;width:14px}
.menu-icon i{display:block;height:1.5px;background:var(--muted);margin-bottom:2.5px}
.brand{left:25px;top:23px;display:flex;align-items:center;gap:8px}
.brand-mark{width:34px;height:34px;border-radius:50%;background:var(--light-dark)}
.brand-name{font-family:'Oswald',sans-serif;font-weight:600;font-size:22px;line-height:1;color:var(--light);letter-spacing:.5px}
.brand-sub{font-family:'Oswald',sans-serif;font-size:5.6px;letter-spacing:1.8px;color:var(--light-dark);margin-top:2px}
.mainnav{left:299px;top:37px;display:flex;gap:33px;font-size:8px;font-weight:500;letter-spacing:.3px}
.headline{left:31px;top:88px;font-size:55px;line-height:45.5px;font-weight:400;letter-spacing:0}
.headline .w{color:var(--white)}.headline .o{color:var(--accent-text)}.headline .t{color:var(--light)}
.vline{left:28px;top:323px;width:1px;height:104px;background:var(--line)}
.rule{left:36px;top:331px;width:25px;height:2px;background:var(--accent-text)}
.kicker{left:36px;top:343px;font-size:8px;color:var(--accent-text);letter-spacing:.3px}
.lede{left:36px;top:358px;font-size:7.4px;line-height:11px;color:var(--muted);font-weight:300}
.btn{background:var(--accent);color:var(--white);display:flex;align-items:center;justify-content:space-between;font-family:'Oswald',sans-serif;font-size:7.5px;letter-spacing:.4px;text-transform:uppercase}
.browse{left:36px;top:394px;width:115px;height:26px;padding:0 11px 0 13px}
.trusted{left:591px;top:86px;width:59px;height:73px;border:1px solid #777;text-align:center;padding-top:8px;color:#d4d4d4}
.trusted .s{font-size:6.5px}.trusted .b{font-size:11px;line-height:13px}
.trusted .stars{font-size:7px;letter-spacing:1px;margin-top:3px}
.sidefeat{left:587px;top:176px;width:1px;height:190px;background:var(--line)}
.feat-s{left:600px;font-size:6px;line-height:9px;color:var(--muted)}
.feat-s svg{display:block;margin-bottom:6px}

/* player */
.player{left:19px;top:449px;width:627px;height:85px;border:1px solid var(--line);background:rgba(30,30,30,.95)}
.cover-sm{left:8px;top:8px;width:53px;height:51px;background:radial-gradient(circle at 50% 30%,#8a8a8a,#303030 80%)}
.track{left:70px;top:18px}
.track .t{font-family:'Oswald',sans-serif;font-size:11px}
.track .a{font-family:'Oswald',sans-serif;font-size:7px;color:var(--muted);margin-top:3px}
.wave{left:139px;top:14px;width:483px;height:33px;
  background:repeating-linear-gradient(90deg,#6e6e6e 0 1px,transparent 1px 2.6px);
  clip-path:polygon(0 48%,4% 38%,8% 30%,12% 35%,16% 20%,20% 28%,24% 12%,28% 25%,32% 18%,36% 8%,40% 22%,44% 15%,48% 26%,52% 10%,56% 20%,60% 14%,64% 5%,68% 22%,72% 16%,76% 24%,80% 12%,84% 20%,88% 8%,92% 22%,96% 18%,100% 40%,100% 60%,96% 82%,92% 78%,88% 92%,84% 80%,80% 88%,76% 76%,72% 84%,68% 78%,64% 95%,60% 86%,56% 80%,52% 90%,48% 74%,44% 85%,40% 78%,36% 92%,32% 82%,28% 75%,24% 88%,20% 72%,16% 80%,12% 65%,8% 70%,4% 62%,0 52%)}
.ctrl{color:var(--white)}
.playbtn{left:300px;top:51px;width:32px;height:32px;border-radius:50%;background:var(--accent);display:flex;align-items:center;justify-content:center}
.time{left:434px;top:61px;font-size:7.5px}.time span{color:var(--muted)}
.vol{left:525px;top:65px;width:58px;height:1px;background:var(--muted)}
.vol i{position:absolute;right:-3px;top:-3px;width:7px;height:7px;border-radius:50%;background:var(--white)}

/* features */
.features{left:19px;top:548px;width:627px;height:75px;background:var(--panel-2);display:flex}
.feature{flex:1;display:flex;align-items:center;gap:12px;padding-left:20px;border-right:1px solid var(--line);margin:10px 0}
.feature:last-child{border-right:0}
.feature h3{font-family:'Oswald',sans-serif;font-weight:500;font-size:9.5px;line-height:11px;color:var(--light-dark);text-transform:uppercase}
.feature p{font-size:6.6px;line-height:10px;color:var(--muted);margin-top:5px}

/* collection */
.sec-title{left:23px;top:645px;font-family:'Oswald',sans-serif;font-weight:500;font-size:16px;color:var(--light-dark);letter-spacing:.5px}
.view-all{left:563px;top:654px;font-family:'Oswald',sans-serif;font-size:7.5px;color:var(--light-dark)}
.cards{left:23px;top:676px;display:flex;gap:10px}
.card{width:115px;height:181px;border:1px solid var(--line);background:var(--panel)}
.card-art{height:112px;display:flex;flex-direction:column;align-items:center;justify-content:center;text-align:center}
.card-art .ttl{font-family:'Oswald',sans-serif;font-weight:600;font-size:17px;letter-spacing:2px;color:#dcdcdc;line-height:1}
.card-art .sub{font-family:'Oswald',sans-serif;font-size:6.5px;letter-spacing:2.6px;color:#c0c0c0;margin-top:3px}
.card h4{font-family:'Oswald',sans-serif;font-weight:500;font-size:10.5px;margin:9px 0 0 7px}
.card .by{font-family:'Oswald',sans-serif;font-size:7px;color:var(--muted);margin:2px 0 0 7px}
.buy{margin:6px 5px 0;height:22px;background:var(--light-dark);color:#262626;display:flex;align-items:center;justify-content:center;gap:4px;font-size:6.5px}
.buy b{font-family:'Oswald',sans-serif;font-weight:500;font-size:9px}
.next{left:653px;top:736px}

/* mindset */
.mindset{left:19px;top:879px;width:627px;height:140px;border:1px solid var(--line);overflow:hidden}
.mindset-art{left:250px;top:0;width:377px;height:140px;background:radial-gradient(ellipse 120px 110px at 120px 60px,#3a3a3a,#222 70%),linear-gradient(90deg,#1b1b1b,#2a2a2a)}
.mindset-fade{left:0;top:0;width:420px;height:140px;background:linear-gradient(90deg,#1c1c1c 55%,rgba(28,28,28,0))}
.mindset h2{left:21px;top:17px;font-family:'Oswald',sans-serif;font-weight:500;font-size:19px;line-height:21px;color:var(--light-dark)}
.mindset p{left:21px;top:67px;font-size:7.4px;line-height:11px;color:var(--muted);font-weight:300}
.join{left:21px;top:100px;width:121px;height:25px;padding:0 11px 0 13px}
.watch{left:467px;top:53px;display:flex;align-items:center;gap:8px;font-family:'Oswald',sans-serif;font-size:10px}

/* badges & footer */
.badges{left:0;top:1041px;width:675px;height:46px;border-top:1px solid var(--line);border-bottom:1px solid var(--line);display:flex;justify-content:space-around;align-items:center;padding:0 25px}
.badge{width:28px;height:28px;border-radius:50%;background:#323232}
.badge.wide{width:100px;height:18px;border-radius:2px}
.f-brand{left:37px;top:1112px}
.f-brand .brand-mark{width:40px;height:40px}
.f-brand .brand-name{font-size:20px}
.fcol{top:1103px;font-size:6.5px;line-height:11.5px;color:var(--dim)}
.fcol h5{font-family:'Oswald',sans-serif;font-weight:400;font-size:6.5px;color:var(--muted);margin-bottom:4px;letter-spacing:.3px}
.fsep{left:418px;top:1100px;width:1px;height:62px;background:var(--line)}
.news{left:445px;top:1103px}
.news h5{font-family:'Oswald',sans-serif;font-weight:400;font-size:8px;color:var(--light-dark)}
.news p{font-size:6.5px;line-height:9.5px;color:var(--dim);margin-top:4px}
.email{left:445px;top:1140px;width:182px;height:21px;border:1px solid var(--line);display:flex;align-items:center;justify-content:space-between;font-size:6.5px;color:var(--dim);padding-left:8px}
.email i{width:24px;height:19px;background:var(--accent);display:flex;align-items:center;justify-content:center}
.bottom{left:15px;top:1170px;width:645px;height:1px;background:var(--line)}
.copy{left:39px;top:1181px;font-size:6.5px;color:var(--dim)}
.social{left:528px;top:1180px;display:flex;gap:16px}
.social i{width:12px;height:12px;border-radius:50%;border:1.5px solid var(--muted)}
</style>
</head>
<body>

<div class="abs hero-art" role="img" aria-label="Silhouetted troops running through dust toward a low sun over mountains"></div>
<div class="abs hero-fade"></div>

<div class="abs topbar cond"><span>Login</span><span>Create Account</span><span>Cart (0)</span><span style="border:0;width:50px"></span></div>
<div class="abs menu-icon"><i></i><i></i><i></i></div>

<div class="abs brand">
  <div class="brand-mark"></div>
  <div><div class="brand-name">MARCHFOLIO</div><div class="brand-sub">MILITARY TRAINING MUSIC</div></div>
</div>
<nav class="abs mainnav cond"><span>Music ⌄</span><span>Playlists</span><span>Support</span><span>About</span><span>Contact</span></nav>

<h1 class="abs headline display"><span class="w">THE</span><br><span class="o">ORIGINAL</span><br><span class="w">VOICE OF</span><br><span class="t">MILITARY</span><br><span class="t">TRAINING</span></h1>
<div class="abs vline"></div>
<div class="abs rule"></div>
<div class="abs kicker">PREMIUM MUSIC. PROVEN RESULTS.</div>
<p class="abs lede">Engineered for intensity. Built for warriors.<br>Trusted by military and tactical athletes worldwide.</p>
<div class="abs btn browse"><span>Browse Catalog</span><span>›</span></div>

<div class="abs trusted cond"><div class="s">Trusted by</div><div class="b">Military<br>Elite</div><div class="s">Worldwide</div><div class="stars">★★★★★</div></div>
<div class="abs sidefeat"></div>
<div class="abs feat-s cond" style="top:193px"><svg width="18" height="14" viewBox="0 0 18 14" fill="none" stroke="#a8a8a8"><path d="M1 7h16M4 4v6M7 1v12M10 3v8M13 5v4"/></svg>High<br>Performance</div>
<div class="abs feat-s cond" style="top:258px"><svg width="14" height="16" viewBox="0 0 14 16" fill="none" stroke="#a8a8a8"><path d="M7 1l6 2v5c0 4-3 6-6 7-3-1-6-3-6-7V3z"/><path d="M7 5v5M5 8l2 2 2-2"/></svg>Uncompromised<br>Quality</div>
<div class="abs feat-s cond" style="top:324px"><svg width="17" height="17" viewBox="0 0 17 17" fill="none" stroke="#a8a8a8"><circle cx="8.5" cy="8.5" r="7"/><circle cx="8.5" cy="8.5" r="4"/><circle cx="8.5" cy="8.5" r="1"/></svg>Mission<br>Focused</div>

<section class="abs player">
  <div class="abs cover-sm" role="img" aria-label="Cover art: soldier against a sunset"></div>
  <div class="abs track"><div class="t">WARCRY 2.0</div><div class="a">MARCHFOLIO</div></div>
  <div class="abs wave"></div>
  <svg class="abs ctrl" style="left:211px;top:61px" width="11" height="9" viewBox="0 0 11 9" fill="none" stroke="#f0f0f0"><path d="M0 1h3l5 7h3M0 8h3l5-7h3M9 0l2 1-2 1M9 7l2 1-2 1"/></svg>
  <svg class="abs ctrl" style="left:275px;top:61px" width="10" height="10" viewBox="0 0 10 10" fill="#f0f0f0"><rect x="0" y="0" width="1.6" height="10"/><path d="M10 0L2 5l8 5z"/></svg>
  <div class="abs playbtn"><svg width="10" height="11" viewBox="0 0 10 11" fill="#fff"><path d="M0 0l10 5.5L0 11z"/></svg></div>
  <svg class="abs ctrl" style="left:348px;top:61px" width="10" height="10" viewBox="0 0 10 10" fill="#f0f0f0"><path d="M0 0l8 5-8 5z"/><rect x="8.4" y="0" width="1.6" height="10"/></svg>
  <svg class="abs ctrl" style="left:373px;top:61px" width="12" height="10" viewBox="0 0 12 10" fill="none" stroke="#f0f0f0"><path d="M2 4V3h8M8 1l2 2-2 2M10 6v1H2M4 9L2 7l2-2"/></svg>
  <div class="abs time">01:24 <span>/ 03:45</span></div>
  <svg class="abs" style="left:508px;top:60px" width="11" height="10" viewBox="0 0 11 10" fill="none" stroke="#f0f0f0"><path d="M1 3h2l3-2v8L3 7H1z"/><path d="M8 3c1 1 1 3 0 4M9.5 1.5c2 2 2 5 0 7"/></svg>
  <div class="abs vol"><i></i></div>
  <svg class="abs" style="left:602px;top:61px" width="11" height="9" viewBox="0 0 11 9" stroke="#f0f0f0"><path d="M0 .5h11M0 3.3h11M0 6h11M0 8.5h11"/></svg>
</section>

<section class="abs features">
  <div class="feature"><svg width="34" height="34" viewBox="0 0 34 34" fill="none" stroke="#6e6e6e" stroke-width="2"><circle cx="17" cy="17" r="13"/><circle cx="17" cy="17" r="6"/><circle cx="17" cy="17" r="2" fill="#6e6e6e"/><path d="M17 0v8M17 26v8M0 17h8M26 17h8"/></svg><div><h3>Curated for<br>Performance</h3><p>Music designed to push<br>limits and drive results.</p></div></div>
  <div class="feature"><svg width="26" height="34" viewBox="0 0 26 34" fill="#6e6e6e"><path d="M0 9L13 0l13 9v6L13 6 0 15zM0 19l13-9 13 9v6l-13-9-13 9zM0 29l13-9 13 9v5l-13-9-13 9z"/></svg><div><h3>Mission<br>Ready</h3><p>Built for the toughest<br>environments.</p></div></div>
  <div class="feature"><svg width="32" height="34" viewBox="0 0 32 34" fill="none" stroke="#6e6e6e" stroke-width="2.5"><path d="M2 3h28v18c0 6-7 10-14 12C9 31 2 27 2 21z"/><path d="M16 9l2.3 5 5.2.4-4 3.4 1.3 5L16 20l-4.8 2.8 1.3-5-4-3.4 5.2-.4z" fill="#6e6e6e" stroke="none"/></svg><div><h3>Elite<br>Quality</h3><p>Professional grade<br>production standards.</p></div></div>
  <div class="feature"><svg width="34" height="34" viewBox="0 0 34 34" fill="none" stroke="#6e6e6e" stroke-width="2"><circle cx="17" cy="17" r="15"/><ellipse cx="17" cy="17" rx="7" ry="15"/><path d="M2 17h30M5 9h24M5 25h24M17 2v30"/></svg><div><h3>Global<br>Trust</h3><p>Used by military units<br>worldwide.</p></div></div>
</section>

<h2 class="abs sec-title">FEATURED COLLECTION</h2>
<div class="abs view-all">VIEW ALL RELEASES &nbsp;&nbsp;›</div>
<section class="abs cards">
  <article class="card"><div class="card-art" role="img" aria-label="Cover art: soldier before a bright sky" style="background:radial-gradient(circle at 50% 35%,#7c7c7c,#333 80%)"><span class="ttl">WARCRY</span><span class="sub">MARCHFOLIO</span></div><h4>WARCRY</h4><div class="by">MARCHFOLIO</div><div class="buy">Buy on <b>Zelpora</b></div></article>
  <article class="card"><div class="card-art" role="img" aria-label="Cover art: soldier aiming through haze" style="background:radial-gradient(circle at 55% 40%,#4a4a4a,#1f1f1f 80%)"><span class="ttl">ENDURE</span><span class="sub">MARCHFOLIO</span></div><h4>ENDURE</h4><div class="by">MARCHFOLIO</div><div class="buy">Buy on <b>Zelpora</b></div></article>
  <article class="card"><div class="card-art" role="img" aria-label="Cover art: soldier advancing through dark smoke" style="background:radial-gradient(circle at 50% 40%,#3a3a3a,#161616 80%)"><span class="ttl">DOMINATE</span><span class="sub">MARCHFOLIO</span></div><h4>DOMINATE</h4><div class="by">MARCHFOLIO</div><div class="buy">Buy on <b>Zelpora</b></div></article>
  <article class="card"><div class="card-art" role="img" aria-label="Cover art: soldier carrying a log in fog" style="background:radial-gradient(circle at 50% 35%,#707070,#2b2b2b 80%)"><span class="ttl" style="font-size:15px">RELENTLESS</span><span class="sub">MARCHFOLIO</span></div><h4>RELENTLESS</h4><div class="by">MARCHFOLIO</div><div class="buy">Buy on <b>Zelpora</b></div></article>
  <article class="card"><div class="card-art" role="img" aria-label="Cover art: soldier in grey mist" style="background:radial-gradient(circle at 50% 35%,#5a5a5a,#1f1f1f 80%)"><span class="ttl" style="font-size:14px">UNBREAKABLE</span><span class="sub">MARCHFOLIO</span></div><h4>UNBREAKABLE</h4><div class="by">MARCHFOLIO</div><div class="buy">Buy on <b>Zelpora</b></div></article>
</section>
<svg class="abs next" width="7" height="10" viewBox="0 0 7 10" fill="none" stroke="#a8a8a8" stroke-width="1.5"><path d="M1 1l4 4-4 4"/></svg>

<section class="abs mindset">
  <div class="abs mindset-art" role="img" aria-label="Soldier wearing headset looking over a dusky landscape"></div>
  <div class="abs mindset-fade"></div>
  <h2 class="abs">MORE THAN MUSIC.<br>IT’S A MINDSET.</h2>
  <p class="abs">Marchfolio delivers the sound of discipline,<br>focus, and victory. Anytime. Anywhere.</p>
  <div class="abs btn join"><span>Join the Movement</span><span>›</span></div>
  <div class="abs watch"><svg width="24" height="24" viewBox="0 0 24 24"><circle cx="12" cy="12" r="11" fill="none" stroke="#f0f0f0" stroke-width="1.3"/><path d="M9.5 7.5l7 4.5-7 4.5z" fill="#f0f0f0"/></svg>WATCH VIDEO</div>
</section>

<section class="abs badges">
  <div class="badge"></div><div class="badge"></div><div class="badge wide"></div><div class="badge"></div><div class="badge"></div><div class="badge"></div>
</section>

<div class="abs brand f-brand">
  <div class="brand-mark"></div>
  <div><div class="brand-name">MARCHFOLIO</div><div class="brand-sub">MILITARY TRAINING MUSIC</div></div>
</div>
<div class="abs fcol" style="left:227px"><h5>COMPANY</h5>About Us<br>Careers<br>Press<br>Contact</div>
<div class="abs fcol" style="left:331px"><h5>SUPPORT</h5>FAQ<br>Help Center<br>Shipping &amp; Returns<br>Terms of Service</div>
<div class="abs fsep"></div>
<div class="abs news"><h5>STAY MISSION READY</h5><p>Subscribe for updates on new releases,<br>exclusive content, and special offers.</p></div>
<div class="abs email"><span>Enter your email</span><i><svg width="6" height="9" viewBox="0 0 6 9" fill="none" stroke="#fff" stroke-width="1.3"><path d="M1 1l3.5 3.5L1 8"/></svg></i></div>
<div class="abs bottom"></div>
<div class="abs copy">© 2024 Marchfolio Military Training Music. All rights reserved.</div>
<div class="abs social"><i></i><i></i><i></i><i></i></div>

</body>
</html>
```